I am a Financial Adviser specialising in Aged Care Advice. We provide financial advice and assistance to families with loved ones entering an Aged Care facility.
We need a flyer detailing the Aged Care Packages that we offer. There will be 3 main packages & then other add ons. I need an area where the client can sign off on the package/s that they choose. I have attached a sample to demonstrate the required layout, and a copy of content. I would like the flyer to have an image as per the attached sample, and to be designed in soft pastels, blues, greens.

Financial

```html
<!DOCTYPE html>
<html lang="en">
<head>
<meta charset="utf-8">
<title>Aged Care Services – Package Selection Flyer</title>
<link href="https://fonts.googleapis.com/css2?family=Roboto:ital,wght@0,400;0,500;0,700;1,700&family=Roboto+Condensed:ital,wght@0,400;0,700;1,700&display=swap" rel="stylesheet">
<style>
:root{
  --lime:#d5e027;
  --title-blue:#1a62b8;
  --navy:#25369a;
  --bright-blue:#0b8fdc;
  --cyan:#22bcd6;
  --mint:#e5f1e4;
  --red:#e2231a;
  --ink:#222;
  --stage:#e9ecee;
}
*{box-sizing:border-box;margin:0;padding:0}
html,body{width:1200px;height:1200px;overflow:hidden}
body{background:var(--stage);position:relative;font-family:"Roboto Condensed",Arial,sans-serif;color:var(--ink)}
.page{position:absolute;top:218px;width:540px;height:765px;overflow:hidden;box-shadow:0 4px 14px rgba(0,0,0,.18)}
.page-front{left:40px;background:linear-gradient(180deg,#fff 0%,#fff 36%,#cdeef3 62%,var(--cyan) 100%)}
.page-back{left:620px;background:#fff}

/* front header */
.header-band{position:absolute;left:0;top:0}
.brand{position:absolute;left:40px;top:24px;font-family:"Roboto",Arial,sans-serif;font-weight:700;font-size:12px;color:var(--navy);letter-spacing:.3px}
.brand::before{content:"";display:inline-block;width:9px;height:9px;background:var(--navy);margin-right:5px;vertical-align:-1px}
.title{position:absolute;left:188px;top:18px;font-family:"Roboto",Arial,sans-serif;font-weight:700;font-size:27px;color:var(--title-blue)}
.photo{position:absolute;left:52px;top:66px;width:429px;height:217px;background:linear-gradient(120deg,#f1e6df 0%,#e4c3ad 40%,#b89a94 70%,#9d8890 100%)}
.photo-curve{position:absolute;left:52px;top:255px}

/* packages */
.pkg-head{position:absolute;left:39px;width:459px;height:40px;border-radius:0 18px 0 18px;background:linear-gradient(90deg,var(--navy) 0%,#1a60c0 55%,var(--bright-blue) 100%);color:#fff;display:flex;align-items:center;padding-left:62px;font-family:"Roboto",Arial,sans-serif;font-weight:700;font-size:12.5px}
.pkg-head .tag{font-family:"Roboto Condensed",sans-serif;font-style:italic;font-size:10px;margin-left:2px}
.check{position:absolute;left:22px;top:9px;width:22px;height:22px;background:#fff;border:1px solid #c9d6ec}
.pkg-body{position:absolute;left:39px;width:459px;background:#fff;font-size:9.5px}
.pkg-body ul{position:absolute;list-style:none}
.pkg-body li{line-height:16.8px;padding-left:16px;position:relative}
.pkg-body li::before{content:"";position:absolute;left:0;top:7px;width:4px;height:4px;border-radius:50%;background:#111}
.pkg-body small{font-size:7px}
.feel{position:absolute;font-family:"Roboto",Arial,sans-serif;font-weight:500;font-size:14px;color:var(--red)}
.plus{position:absolute;left:35px;font-weight:700;font-size:9.5px;color:var(--navy)}
.note{position:absolute;left:37px;top:75px;font-size:7.5px;color:#666}
.note span,.star{color:var(--red)}

/* back */
.back-mint{position:absolute;left:0;top:0;width:540px;height:518px;background:var(--mint)}
.back-title{position:absolute;left:59px;top:30px;font-family:"Roboto",Arial,sans-serif;font-weight:700;font-size:12.5px;color:var(--title-blue)}
.option{position:absolute;left:48px;width:453px;height:64px}
.option svg{position:absolute;left:0;top:0}
.option .check{left:6px;top:5px;width:18px;height:18px}
.option-name{position:absolute;left:33px;top:7px;color:#fff;font-weight:700;font-size:10px}
.option-desc{position:absolute;left:28px;top:38px;width:420px;font-size:7.3px;line-height:10.6px}
.agree{position:absolute;left:46px;top:538px;width:455px;font-size:8.6px;line-height:16.6px;color:#333}
.sig{position:absolute;top:600px;width:90px;border-top:1px solid #333;font-size:7.3px;text-align:center;padding-top:6px}
.date{position:absolute;left:400px;top:590px;font-size:9px;letter-spacing:1px}
.info{position:absolute;left:46px;top:654px;width:455px;font-size:6.4px;line-height:8.4px;color:#333}
.info h4{font-size:6.8px;font-weight:700;color:#111}
.info p{margin-bottom:6px}
</style>
</head>
<body>

<section class="page page-front">
  <svg class="header-band" width="540" height="110" viewBox="0 0 540 110">
    <path d="M0 0H540L482 50Q468 66 440 66H0Z" fill="var(--lime)"/>
  </svg>
  <div class="brand">Harbourline</div>
  <h1 class="title">Aged Care Services</h1>
  <div class="photo" role="img" aria-label="Close-up of a carer's hands gently holding an elderly person's hands"></div>
  <svg class="photo-curve" width="80" height="30" viewBox="0 0 80 30"><path d="M0 30V22Q8 2 40 0H0V30" fill="none"/><path d="M0 28Q6 6 40 1V30H0Z" fill="none"/></svg>

  <div class="pkg-head" style="top:310px"><span class="check"></span>ESSENTIALS Package $770<span class="tag">&nbsp;…When you know what you want…</span></div>
  <div class="pkg-body" style="top:350px;height:93px">
    <div class="feel" style="left:336px;top:7px">Peace of Mind</div>
    <ul style="left:23px;top:14px">
      <li>Explanation of Aged Care Fees and Charges.</li>
      <li>Preliminary Home/Assets Assessment.<span class="star">*</span></li>
      <li>Estimated Means Tested Fee Calculation.<span class="star">*</span></li>
    </ul>
    <ul style="left:252px;top:31px">
      <li>Preliminary Aged Care Costs.<span class="star">*</span></li>
      <li>Estimated Cash Flow Scenario.<span class="star">*</span></li>
    </ul>
    <div class="note"><span>*</span>Please note this is general factual information only.&nbsp; We do not provide any specific personal information.</div>
  </div>

  <div class="pkg-head" style="top:455px"><span class="check"></span>ADVANTAGE Package $2,970<span class="tag">…When you need to know all the options…</span></div>
  <div class="pkg-body" style="top:495px;height:88px">
    <div class="plus" style="top:16px">ESSENTIALS Package plus</div>
    <div class="feel" style="left:344px;top:8px">Confidence</div>
    <ul style="left:23px;top:31px">
      <li>Analyse and Strategize Aged Care costs.</li>
      <li>Compare up to 5 Strategy options.</li>
      <li>Minimise Aged Care Costs <small>(where possible).</small></li>
    </ul>
    <ul style="left:252px;top:31px">
      <li>Maximise Age Pension Income <small>(where possible).</small></li>
      <li>Prepare a Full Statement of Advice <small>(SOA).</small></li>
      <li>Implementation of Aged Care Strategy.</li>
    </ul>
  </div>

  <div class="pkg-head" style="top:600px"><span class="check"></span>PLATINUM Package $5,940<span class="tag">…When you need someone to take charge…</span></div>
  <div class="pkg-body" style="top:640px;height:93px">
    <div class="plus" style="top:16px">ADVANTAGE Package plus</div>
    <div class="feel" style="left:339px;top:10px">Convenience</div>
    <ul style="left:23px;top:31px">
      <li>Liase with the Aged Care Facility.</li>
      <li>CentreLink/DVA Nominee.</li>
      <li>Post Entry Review.</li>
    </ul>
    <ul style="left:252px;top:48px">
      <li>Post Implementation SOA (if required).</li>
      <li>Annual Review.</li>
    </ul>
  </div>
</section>

<section class="page page-back">
  <div class="back-mint"></div>
  <h2 class="back-title">EXTRA CHOICE OPTIONS</h2>

  <div class="option" style="top:61px">
    <svg width="453" height="30"><path d="M0 1H262Q248 26 220 29H0Z" fill="url(#bar)"/><rect x="0" y="0" width="453" height="2" fill="var(--bright-blue)"/>
      <defs><linearGradient id="bar"><stop offset="0" stop-color="var(--navy)"/><stop offset="1" stop-color="var(--bright-blue)"/></linearGradient></defs></svg>
    <span class="check"></span><div class="option-name">CentreLink/DVA Nominee $1,100</div>
    <p class="option-desc">Communicate with CentreLink/DVA on behalf of our client/s, and undertake all changes and updates to details, as directed by our client.</p>
  </div>
  <div class="option" style="top:125px">
    <svg width="453" height="30"><path d="M0 1H262Q248 26 220 29H0Z" fill="url(#bar)"/><rect width="453" height="2" fill="var(--bright-blue)"/></svg>
    <span class="check"></span><div class="option-name">Post Implementation Statement of Advice $1,650</div>
    <p class="option-desc">Revise our original Advice Statement for any changes of circumstances including income &amp; asset variations, and provide further advice within the first 12 months of initial advice statement.</p>
  </div>
  <div class="option" style="top:189px">
    <svg width="453" height="30"><path d="M0 1H262Q248 26 220 29H0Z" fill="url(#bar)"/><rect width="453" height="2" fill="var(--bright-blue)"/></svg>
    <span class="check"></span><div class="option-name">Annual Review $990</div>
    <p class="option-desc">A review of the recommendations made in our original advice document, taking into account any changes to client's circumstances including checking current cash flow is sufficient to meet ongoing aged care costs.</p>
  </div>
  <div class="option" style="top:253px">
    <svg width="453" height="30"><path d="M0 1H262Q248 26 220 29H0Z" fill="url(#bar)"/><rect width="453" height="2" fill="var(--bright-blue)"/></svg>
    <span class="check"></span><div class="option-name">Post Entry Review $660</div>
    <p class="option-desc">Review financial situation, check facility invoices are accurate, explain the Residential Aged Care Agreement and ensure all recommendations are implemented.</p>
  </div>
  <div class="option" style="top:317px">
    <svg width="453" height="30"><path d="M0 1H262Q248 26 220 29H0Z" fill="url(#bar)"/><rect width="453" height="2" fill="var(--bright-blue)"/></svg>
    <span class="check"></span><div class="option-name">Facility Liason $550</div>
    <p class="option-desc">Negotiate with the Aged Care Facility regarding Accommodation payments, clarify &amp; explain Residential Care Agreement, and review facility invoices.</p>
  </div>
  <div class="option" style="top:381px">
    <svg width="453" height="30"><path d="M0 1H262Q248 26 220 29H0Z" fill="url(#bar)"/><rect width="453" height="2" fill="var(--bright-blue)"/></svg>
    <span class="check"></span><div class="option-name">Family Conferences $660</div>
    <p class="option-desc">Facilitate &amp; co-ordinate family meetings to explain the Aged Care legislation and how it fits with the family circumstances.</p>
  </div>
  <div class="option" style="top:445px">
    <svg width="453" height="30"><path d="M0 1H262Q248 26 220 29H0Z" fill="url(#bar)"/><rect width="453" height="2" fill="var(--bright-blue)"/></svg>
    <span class="check"></span><div class="option-name">Estate Wrap $660</div>
    <p class="option-desc">Assist beneficiaries with correct procedures and paperwork regarding the finalisation of the estate.</p>
  </div>

  <p class="agree">I/We have chosen the Service Package and Options as ticked above.&nbsp; I/We understand that by choosing the Essentials Package, that I/We are receiving factual information only, and not financial advice.&nbsp; I/We agree to pay the amount of ………………….., within seven days of the date of the invoice received from Harbourline Advisory SA.</p>

  <div class="sig" style="left:46px">Signature</div>
  <div class="sig" style="left:163px">Signature</div>
  <div class="sig" style="left:282px">Signature</div>
  <div class="date">____/____/____</div>

  <div class="info">
    <h4>Important Information</h4>
    <p>This document has been prepared by Harbourline Advisory SA Pty Ltd ABN 00 000 000 000, an Authorised Representative of Northgate Advice Limited ABN 00 000 000 001 AFSL 000000, a wholly owned, non-guaranteed subsidiary of the Southern Mutual Bank ABN 00 000 000 002.</p>
    <p>Information in this document is based on current regulatory requirements and laws, as at 20 September, 2016 which may be subject to change.&nbsp; It contains general advice.&nbsp; It does not take into account your individual objectives, financial situation or needs.&nbsp; You should consider talking to a financial adviser before making a financial decision.</p>
  </div>
</section>

</body>
</html>
```